Wordpress template re-design of current website

We need a WordPress template design and new look for our existing website. Our existing site it located at www.velmoro.com.au We are a tech company and want a fresh, clean modern website that matches our brand, services and logo colors. Our main Services are hospitality solutions, Velmoro TV solution and managed networks, more information on these can come from our existing website.

Target Market(s)

We are a tech company so must have a modern feel for new technology

Industry/Entity Type

It Company

Number of Pages Required

5+ page

Font styles to use
Sans Serif

Requirements
Must have
• Be based on a wordpress templete design and match the services that we have in our existing website, in the testimonials want a place for video testimonials as well as text. Nice clean icons used for graphics to represent services.
Nice to have
• nice visual representation of our services in the way of clean icons etc
Should not have
• Clutter

```html
<!DOCTYPE html>
<html lang="en">
<head>
<meta charset="utf-8">
<title>Velmoro Wireless Internet – Services</title>
<link href="https://fonts.googleapis.com/css2?family=Roboto:wght@400;500;700&family=Roboto+Condensed:wght@400;700&family=Roboto+Slab:wght@400;500&display=swap" rel="stylesheet">
<style>
:root{
  --navy:#0b3f86;
  --navy-dark:#0a3570;
  --teal:#1b96c3;
  --slate:#5f707f;
  --slate-light:#75848f;
  --ink:#333;
  --muted:#6b7680;
  --band:#ececec;
  --footer:#3b3c3e;
  --bar:#5f6b75;
  --white:#fff;
}
*{margin:0;padding:0;box-sizing:border-box}
html,body{width:899px;height:1200px;overflow:hidden;background:var(--white);font-family:"Roboto",Arial,sans-serif;color:var(--ink)}
.page{position:relative;width:899px;height:1200px}
.abs{position:absolute}
.topbar{left:0;top:0;width:899px;height:27px;background:var(--navy);border-bottom:2px solid #c9d2dd}
.tagline{left:247px;top:6px;font:400 12px "Roboto Slab",serif;color:var(--white)}
.portal{left:590px;top:0;width:52px;height:31px;background:#6f7c86;color:var(--white);font:400 12px "Roboto Slab",serif;text-align:center;padding-top:6px}
.follow{left:668px;top:8px;font:500 9.5px "Roboto",sans-serif;color:var(--white)}
.social{top:6px;width:15px;height:15px;border-radius:50%;background:#8a97a6}
.logo{left:100px;top:36px;font:400 31px "Roboto",sans-serif;color:var(--navy);letter-spacing:-.5px;line-height:36px}
.logo-sub{left:113px;top:64px;font:400 8.5px "Roboto",sans-serif;color:var(--navy);letter-spacing:1px}
.logo-dot{left:224px;top:42px;width:24px;height:24px;border-radius:50%;background:var(--navy)}
.nav{left:293px;top:56px;display:flex;font:400 11px "Roboto Slab",serif;color:#222}
.nav span{padding:0 7px;border-left:1px solid var(--navy);line-height:14px}
.nav span:first-child{border-left:0;padding-left:0}
.nav .active{color:var(--navy);font-weight:500}
.call-label{left:717px;top:42px;font:400 10px "Roboto Condensed",sans-serif;color:var(--muted)}
.call-num{left:717px;top:53px;font:400 16px "Roboto",sans-serif;color:var(--navy)}
.hdr-line{left:0;top:81px;width:899px;height:1px;background:#dde2e7}
.hero{left:0;top:82px;width:899px;height:306px;background:linear-gradient(90deg,#9aa0a5 0%,#c9ccce 25%,#e8eaec 55%,#f3f5f7 100%)}
.hero-text{right:95px;top:207px;text-align:right;font:400 19px/30px "Roboto Condensed",sans-serif;color:#333}
.arrow{top:210px;width:26px;height:24px;background:#3a3d40;color:var(--white);font:700 13px sans-serif;text-align:center;line-height:24px}
.sec-title{left:99px;top:413px;font:400 20px "Roboto Condensed",sans-serif;color:var(--navy)}
.sec-title em{font-style:normal;color:var(--slate)}
.sec-rule{left:99px;top:446px;width:457px;height:1px;background:#ccc}
.sec-rule-accent{left:99px;top:445px;width:55px;height:3px;background:var(--navy)}
.tabs{left:99px;top:473px;width:174px}
.tab{position:relative;height:50px;background:var(--slate-light);border-bottom:2px solid #c5ccd2;color:var(--white);font:400 12px/14px "Roboto Condensed",sans-serif;padding:10px 0 0 61px}
.tab.active{background:var(--teal)}
.tab.active::after{content:"";position:absolute;right:-7px;top:18px;border:7px solid transparent;border-right:0;border-left-color:var(--teal)}
.tab svg{position:absolute;left:16px;top:12px}
.content{left:298px;top:473px;width:505px}
.content h2{font:400 14px "Roboto Condensed",sans-serif;color:var(--navy);margin-bottom:6px}
.content p{font:400 8.6px/14.3px "Roboto",sans-serif;color:#333;margin-bottom:6px}
.content h3{font:400 14px "Roboto Condensed",sans-serif;color:var(--navy);margin:9px 0 6px}
.benefits li{list-style:none;font:400 8.6px/17px "Roboto",sans-serif;color:#333;display:flex;align-items:center;gap:5px}
.benefits b{font-weight:400;color:var(--navy)}
.clients{left:0;top:764px;width:899px;height:162px;background:var(--band)}
.clients-title{left:0;top:791px;width:899px;text-align:center;font:400 14px "Roboto Condensed",sans-serif;color:var(--navy)}
.clients-title em{font-style:normal;color:var(--slate)}
.clients-rule{left:200px;top:816px;width:499px;height:1px;background:#c8c8c8}
.clients-accent{left:424px;top:815px;width:51px;height:3px;background:var(--navy)}
.client-row{left:100px;top:836px;display:flex;gap:11px}
.client{width:79px;height:53px;background:var(--white);border:1px solid #d2d2d2;display:flex;align-items:center;justify-content:center;font:700 11px "Roboto",sans-serif;color:#444}
.footer{left:0;top:926px;width:899px;height:248px;background:linear-gradient(135deg,#424345,#353638 60%,#3d3e40)}
.contact{left:100px;top:940px;width:270px;color:var(--white)}
.contact h4{font:400 14px "Roboto Condensed",sans-serif;padding:0 0 5px 20px;border-bottom:1px dashed #888;display:inline-block;margin-bottom:9px}
.c-item{position:relative;padding-left:24px;font:400 9.6px/13.8px "Roboto",sans-serif;margin-bottom:10px;white-space:nowrap}
.c-item svg{position:absolute;left:0;top:2px}
.f-logo{left:365px;top:1046px;font:400 38px "Roboto",sans-serif;color:#8e9092}
.f-logo-sub{left:382px;top:1088px;font:400 11px "Roboto",sans-serif;color:#8e9092;letter-spacing:1.5px}
.inquiry{left:590px;top:938px;width:215px;height:224px;background:rgba(110,112,116,.85);border-top:2px solid #c9ccd0;padding:12px 10px}
.inq-head{display:flex;align-items:center;gap:8px;font:400 17px "Roboto Condensed",sans-serif;color:var(--white)}
.inq-icon{width:29px;height:29px;border-radius:50%;background:var(--white);display:flex;align-items:center;justify-content:center}
.inq-sub{font:400 8.6px "Roboto",sans-serif;color:var(--white);margin:12px 0 7px}
.field{height:22px;background:rgba(255,255,255,.12);border-bottom:1px solid rgba(255,255,255,.15);margin-bottom:3px;font:400 8.6px "Roboto",sans-serif;color:#e6e6e6;padding:6px 7px}
.field.tall{height:36px}
.submit{margin-top:7px;width:82px;height:22px;background:var(--navy);color:var(--white);font:500 11px "Roboto",sans-serif;text-align:center;line-height:22px;letter-spacing:.5px}
.bottombar{left:0;top:1174px;width:899px;height:26px;background:var(--bar)}
.bb-links{left:100px;top:1180px;display:flex;font:400 11px "Roboto Condensed",sans-serif;color:var(--white)}
.bb-links span{display:flex;align-items:center;gap:5px;padding:0 15px;border-left:1px solid #7f8a93}
.bb-links span:first-child{border-left:0;padding-left:0}
.copy{right:95px;top:1181px;font:400 8.6px "Roboto",sans-serif;color:var(--white)}
</style>
</head>
<body>
<div class="page">
  <header>
    <div class="abs topbar"></div>
    <div class="abs tagline">Revolutionising HSIA Seervice</div>
    <div class="abs portal">Portal</div>
    <div class="abs follow">Follow Us On</div>
    <div class="abs social" style="left:733px"></div>
    <div class="abs social" style="left:757px"></div>
    <div class="abs social" style="left:782px"></div>

    <div class="abs logo-dot"></div>
    <div class="abs logo">Velmoro</div>
    <div class="abs logo-sub">wireless&nbsp;&nbsp;internet</div>

    <nav class="abs nav">
      <span>Home</span><span>About Us</span><span class="active">Services</span><span>Our Work</span><span>Video Testimonials</span><span>Contact Us</span>
    </nav>
    <svg class="abs" style="left:690px;top:45px" width="22" height="22" viewBox="0 0 22 22"><circle cx="11" cy="11" r="10" fill="none" stroke="#7b858e" stroke-width="1.2"/><path d="M8 6c-1 1-1 3 1 6s4 4 5 4l1-1-2-2-1 1c-1-.5-2-2-2.5-3l1-1-2-2z" fill="#7b858e"/></svg>
    <div class="abs call-label">Call Us Today</div>
    <div class="abs call-num">1300 555 214</div>
    <div class="abs hdr-line"></div>
  </header>

  <section>
    <div class="abs hero" role="img" aria-label="Photo of a hand using a tablet with a stylus on a bright desk"></div>
    <div class="abs hero-text">We Have Been A Leader In Wireless<br>Networks for Home Systems<br>For Over A Decade</div>
    <div class="abs arrow" style="left:4px">&lsaquo;</div>
    <div class="abs arrow" style="left:868px">&rsaquo;</div>
  </section>

  <section>
    <div class="abs sec-title">Services <em>We Provide</em></div>
    <div class="abs sec-rule"></div>
    <div class="abs sec-rule-accent"></div>

    <div class="abs tabs">
      <div class="tab active"><svg width="28" height="24" viewBox="0 0 28 24"><path d="M2 4h24M4 4v18M24 4v18M4 16h20M4 12h6v4H4zM11 12h13v4H11z" fill="none" stroke="#fff" stroke-width="1.6"/></svg>Hospitality<br>Solutions</div>
      <div class="tab"><svg width="28" height="24" viewBox="0 0 28 24"><rect x="2" y="3" width="24" height="15" fill="none" stroke="#fff" stroke-width="1.8"/><path d="M9 21h10" stroke="#fff" stroke-width="1.8"/></svg>Velmoro<br>TV Solution</div>
      <div class="tab"><svg width="28" height="24" viewBox="0 0 28 24"><circle cx="13" cy="12" r="10" fill="none" stroke="#fff" stroke-width="1.8"/><path d="M5 8l16 8M9 3l8 18M3 14l18-6" stroke="#fff" stroke-width="1.4"/></svg>Managed<br>Networks</div>
      <div class="tab"><svg width="32" height="24" viewBox="0 0 32 24"><circle cx="7" cy="8" r="3.5" fill="none" stroke="#fff" stroke-width="1.6"/><path d="M1 20c0-5 12-5 12 0zM14 20h16l-2-7H16z" fill="none" stroke="#fff" stroke-width="1.6"/></svg>Mining And<br>Remote Service</div>
    </div>

    <div class="abs content">
      <h2>Get On The Fastest, Most Flexible Internet Access System</h2>
      <p>Our high quality Wi Fi networks offer a robust 24/7 connectivity, enhancing our client's hospitality services. Whether travelling for business or pleasure, guests like to stay connected with their families, friends, and more importantly, with their work. Velmoro's award-winning gateway devices provide an exceptional, easy-to-use interface that delivers on our exceptional service.</p>
      <p>We back our words with an expert support team. If the system faces any issues highly trained technicians are available on the spot to remedy the problem. Our advanced systems integrate easily with the client's current IT system offering advanced options such as paid access, which can be charged directly to the room account. Another option we provide is payment through credit cards or by vouchers created from our club-based customer portal.</p>
      <p>The sole focus of Velmoro's hospitality solutions is to make them an intuitive, guest friendly experience.</p>
      <h3>Advantage to Use Our Service</h3>
      <ul class="benefits">
        <li><svg width="10" height="10" viewBox="0 0 10 10"><circle cx="5" cy="5" r="4" fill="none" stroke="#555"/><path d="M3 5l1.6 1.6L9 1.5" fill="none" stroke="#555" stroke-width="1.2"/></svg><span><b>Custom designed login pages</b> - We design login pages that reflect our client's brand.</span></li>
        <li><svg width="10" height="10" viewBox="0 0 10 10"><circle cx="5" cy="5" r="4" fill="none" stroke="#555"/><path d="M3 5l1.6 1.6L9 1.5" fill="none" stroke="#555" stroke-width="1.2"/></svg><span><b>Easy to use</b> - Our systems are adapted for mobile and tablet use as well.</span></li>
        <li><svg width="10" height="10" viewBox="0 0 10 10"><circle cx="5" cy="5" r="4" fill="none" stroke="#555"/><path d="M3 5l1.6 1.6L9 1.5" fill="none" stroke="#555" stroke-width="1.2"/></svg><span><b>Complete PMS intergration</b> - Guests can charge their internet access directly to their room account.</span></li>
        <li><svg width="10" height="10" viewBox="0 0 10 10"><circle cx="5" cy="5" r="4" fill="none" stroke="#555"/><path d="M3 5l1.6 1.6L9 1.5" fill="none" stroke="#555" stroke-width="1.2"/></svg><span><b>Full support options</b> - 24/7 monitoring backed by 24/7 support centre</span></li>
      </ul>
    </div>
  </section>

  <section>
    <div class="abs clients"></div>
    <div class="abs clients-title">Our <em>Clients</em></div>
    <div class="abs clients-rule"></div>
    <div class="abs clients-accent"></div>
    <div class="abs client-row">
      <div class="client">Pellowin</div>
      <div class="client">Zuvaro</div>
      <div class="client">Keldarra</div>
      <div class="client">Marrowind</div>
      <div class="client">Tulvane</div>
      <div class="client">Brennock</div>
      <div class="client">Keldarra</div>
      <div class="client">Zuvaro</div>
    </div>
  </section>

  <footer>
    <div class="abs footer" role="img" aria-label="Dark street map of the local area behind the footer"></div>
    <div class="abs f-logo">Velmoro</div>
    <div class="abs f-logo-sub">wireless&nbsp;&nbsp;&nbsp;internet</div>

    <div class="abs contact">
      <h4>Contact Information</h4>
      <div class="c-item"><svg width="11" height="14" viewBox="0 0 11 14"><path d="M5.5 0a5 5 0 0 0-5 5c0 4 5 9 5 9s5-5 5-9a5 5 0 0 0-5-5z" fill="#fff"/><circle cx="5.5" cy="5" r="1.8" fill="#3b3c3e"/></svg>Postal Address<br>48 Harbour Crescent, Coral Bay, QLD 4230</div>
      <div class="c-item"><svg width="12" height="12" viewBox="0 0 12 12"><path d="M2 1c-1.5 1.5-1 4 1.5 6.5S8.5 11 10 9.5L8 7.5 6.8 8.5C5.5 8 4 6.5 3.5 5.2L4.5 4z" fill="#fff"/></svg>Telephone<br>1300 555 214 &amp; Fax: 456-555-0192</div>
      <div class="c-item"><svg width="12" height="10" viewBox="0 0 12 10"><rect x="0" y="1" width="12" height="8" fill="#fff"/><path d="M0 1l6 4 6-4" fill="none" stroke="#3b3c3e"/></svg>Email<br>Information and Support: hello@velmoro-net.com</div>
      <div class="c-item"><svg width="10" height="10" viewBox="0 0 10 10"><rect width="10" height="10" fill="#fff"/></svg>Facebook<br>www.facebook.com/VelmoroWireless</div>
      <div class="c-item"><svg width="10" height="10" viewBox="0 0 10 10"><rect width="10" height="10" fill="#fff"/></svg>Twitter<br>www.twitter.com/VelmoroWireless</div>
    </div>

    <div class="abs inquiry">
      <div class="inq-head"><div class="inq-icon"><svg width="14" height="14" viewBox="0 0 12 12"><path d="M2 1c-1.5 1.5-1 4 1.5 6.5S8.5 11 10 9.5L8 7.5 6.8 8.5C5.5 8 4 6.5 3.5 5.2L4.5 4z" fill="#0b3f86"/></svg></div>Quick Inquiry</div>
      <div class="inq-sub">Lorem ipsum dolor sit amet, consectetuer</div>
      <div class="field">Name</div>
      <div class="field">Email</div>
      <div class="field">Phone</div>
      <div class="field tall">Message</div>
      <div class="submit">SUBMIT</div>
    </div>

    <div class="abs bottombar"></div>
    <div class="abs bb-links">
      <span><svg width="10" height="10" viewBox="0 0 10 10"><circle cx="5" cy="5" r="5" fill="#fff"/><path d="M2.8 5l1.6 1.6L7.5 3.2" fill="none" stroke="#1b96c3" stroke-width="1.4"/></svg>Case Studies</span>
      <span><svg width="10" height="10" viewBox="0 0 10 10"><circle cx="5" cy="5" r="5" fill="#fff"/><path d="M2.8 5l1.6 1.6L7.5 3.2" fill="none" stroke="#1b96c3" stroke-width="1.4"/></svg>News</span>
      <span><svg width="10" height="10" viewBox="0 0 10 10"><circle cx="5" cy="5" r="5" fill="#fff"/><path d="M2.8 5l1.6 1.6L7.5 3.2" fill="none" stroke="#1b96c3" stroke-width="1.4"/></svg>Resellers</span>
    </div>
    <div class="abs copy">© 2015&nbsp; VelmoroWirelessInternet&nbsp; All rights reserved</div>
  </footer>
</div>
</body>
</html>
```